i need a template design for online store

hi great designers, i need a template for any online store. But preferably well owned shopping carts. I would be an added advantage if the store is setup for me. I need a mature and attractive colours. My online store deals in electronics.

Shopping

1 page

```html
<!DOCTYPE html>
<html lang="en">
<head>
<meta charset="utf-8">
<title>Electronics Store – Desktop</title>
<link rel="stylesheet" href="https://fonts.googleapis.com/css2?family=Open+Sans:wght@400;600;700&display=swap">
<style>
:root{
  --green:#6b9a1e;
  --green-dark:#5a8515;
  --green-light:#7fae2c;
  --lime:#a4c13f;
  --page:#f4f4f4;
  --grey:#e3e3e3;
  --grey-mid:#d0d0d0;
  --grey-dark:#bdbdbd;
  --text:#3a3a3a;
  --muted:#666;
  --white:#fff;
}
*{box-sizing:border-box;margin:0;padding:0}
html,body{width:1200px;height:2341px;overflow:hidden}
body{position:relative;background:var(--page);font-family:"Open Sans",Arial,sans-serif;color:var(--text)}
.abs{position:absolute}
ul{list-style:none}

/* top bar */
.topbar{left:0;top:0;width:1200px;height:33px}
.topbar-inner{left:166px;width:868px;height:33px;background:var(--green)}
.top-link{top:0;height:33px;line-height:33px;font-size:12px;color:var(--white);display:flex;align-items:center;gap:6px}
.top-link.home{left:166px;width:70px;background:var(--white);color:var(--green);justify-content:center}
.top-select{top:2px;height:29px;border:1px solid rgba(255,255,255,.5);background:var(--green-dark);color:var(--white);font-size:12px;display:flex;align-items:center;gap:6px;padding:0 8px}

/* header */
.header{left:0;top:33px;width:1200px;height:88px;background:var(--white)}
.logo{left:168px;top:58px;font-size:32px;font-weight:700;color:var(--green);letter-spacing:1px}
.logo span{color:#555}
.account{left:747px;top:70px;font-size:12px;color:var(--green);font-weight:600}
.account em{font-style:normal;color:var(--muted)}
.head-icon{top:62px;width:28px;height:28px;border:2px solid var(--green);border-radius:3px}
.badge{top:-9px;right:-9px;width:16px;height:16px;border-radius:50%;background:var(--green);color:#fff;font-size:9px;text-align:center;line-height:16px}

/* nav */
.nav{left:0;top:121px;width:1200px;height:35px;background:#ececec}
.nav-item{top:121px;height:35px;line-height:35px;font-size:12.5px;color:var(--green);font-weight:600}
.nav-item.active{top:124px;height:29px;line-height:29px;padding:0 10px;background:var(--green);color:#fff}
.search{left:810px;top:127px;width:197px;height:24px;background:#fff;border:1px solid #ccc;font-size:11px;color:#888;padding-left:8px;line-height:22px}
.search-btn{left:1007px;top:127px;width:27px;height:24px;background:var(--green)}

/* breadcrumb */
.crumb{left:166px;top:172px;width:868px;height:27px;background:var(--green);color:#fff;font-size:13px;font-weight:700;line-height:27px;padding-left:10px}

/* banner */
.promo{left:170px;top:234px;width:638px;height:160px;border:2px dashed #c9d98f;background:linear-gradient(90deg,#b6cd62,#e8e985 55%,#eaea93)}
.promo-title{left:30px;top:28px;font-size:35px;font-weight:600;line-height:48px;color:#333;letter-spacing:1px}
.promo-offer{left:450px;top:-2px;width:188px;height:160px;background:var(--green);color:#fff;font-size:34px;font-weight:600;text-align:center;line-height:50px;padding-top:28px;letter-spacing:1px}

/* products */
.grid{left:168px;top:429px;display:grid;grid-template-columns:repeat(3,201px);grid-auto-rows:264px;column-gap:21px;row-gap:27px}
.card{position:relative;background:var(--grey)}
.card-media{position:absolute;left:0;top:0;width:201px;height:199px;background:#fff;border:1px solid #ddd}
.card-media i{position:absolute;display:block;border-radius:6px}
.card-name{position:absolute;left:10px;top:199px;width:181px;height:19px;background:#fff;text-align:center;font-size:12px;line-height:19px;color:var(--green)}
.card-price{position:absolute;left:0;top:224px;width:201px;text-align:center;font-size:15px;color:#333}
.stars{position:absolute;left:70px;top:248px;display:flex;gap:2px}
.stars b{width:11px;height:11px;background:var(--green)}

/* sidebar */
.side-head{left:831px;width:203px;height:26px;background:var(--green);color:#fff;font-size:14px;line-height:26px;padding-left:6px;letter-spacing:.5px}
.side-list{left:840px;font-size:12px;color:#444;line-height:22.3px;text-transform:uppercase}
.side-list li::before{content:"";display:inline-block;width:5px;height:5px;background:#333;border-radius:50%;margin:0 9px 2px 0}
.side-list.boxes li::before{width:8px;height:8px;border-radius:0;background:#fff;border:1px solid #777}
.side-list li.on{color:var(--green)}
.side-list.boxes li.on::before{background:var(--green);border-color:var(--green)}
.ad{left:831px;width:203px;background:var(--grey-dark);color:#fff;font-size:34px;font-weight:600;padding:30px 0 0 16px;line-height:52px;letter-spacing:1px}

/* features */
.features{left:0;top:1674px;width:1200px;height:90px;background:var(--green)}
.feature{top:1686px;width:202px;height:64px;background:var(--green-light);border:1px solid #9dc553;color:#fff;display:flex;align-items:center;gap:12px;padding-left:14px}
.feature strong{display:block;font-size:15px;font-weight:400}
.feature small{display:block;font-size:10px}

/* brands */
.section-title{left:523px;top:1848px;width:156px;height:41px;background:var(--green);color:#fff;font-size:21px;text-align:center;line-height:41px;letter-spacing:1px}
.brand{top:1912px;width:129px;height:59px;background:#fff;border:1px solid #ddd;display:flex;align-items:center;justify-content:center;gap:7px;font-size:14px;font-weight:600;color:#4a4a4a}
.brand i{width:12px;height:12px;background:var(--green)}

/* footer */
.footer{left:0;top:2015px;width:1200px;height:233px;background:#e8e8e8}
.foot-col{top:2062px;width:202px}
.foot-col h4{font-size:15px;font-weight:400;color:var(--green);letter-spacing:1px;padding-bottom:6px;border-bottom:2px solid #555;margin-bottom:10px}
.foot-col li{font-size:11.5px;line-height:22px;color:#444;text-transform:uppercase;padding-left:14px;position:relative}
.foot-col li::before{content:"";position:absolute;left:2px;top:10px;width:4px;height:4px;background:#333;border-radius:50%}
.contact li{padding-left:22px}
.contact li::before{display:none}
.contact svg{position:absolute;left:2px;top:5px}

.paybar{left:0;top:2248px;width:1200px;height:46px;background:#dcdcdc}
.tag{top:2256px;height:30px;background:var(--green);color:#fff;font-size:14px;line-height:30px;text-align:center}
.pay{top:2256px;width:52px;height:32px;background:#fff;border:1px solid #b8b8b8;font-size:9.5px;font-weight:600;color:#2d4a8a;text-align:center;line-height:30px}
.social{top:2256px;width:34px;height:34px;border-radius:3px;color:#fff;font-size:8px;font-weight:600;text-align:center;line-height:34px}
.copy{left:0;top:2294px;width:1200px;height:47px;background:var(--green);color:#dfe9c5;font-size:15px;text-align:center;line-height:47px}
</style>
</head>
<body>

<!-- top bar -->
<div class="abs topbar-inner" style="top:0"></div>
<div class="abs top-link home">
  <svg width="11" height="11" viewBox="0 0 12 12"><path d="M1 6 6 1l5 5v5H7V8H5v3H1z" fill="currentColor"/></svg>Home</div>
<div class="abs top-link" style="left:246px">
  <svg width="11" height="11" viewBox="0 0 12 12"><circle cx="6" cy="3.5" r="2.5" fill="#fff"/><path d="M1 12c0-4 10-4 10 0z" fill="#fff"/></svg>My Account</div>
<div class="abs top-link" style="left:353px">
  <svg width="12" height="11" viewBox="0 0 12 11"><path d="M0 1h2l2 6h6l2-5H3" fill="none" stroke="#fff" stroke-width="1.4"/><circle cx="5" cy="9.5" r="1.2" fill="#fff"/><circle cx="9" cy="9.5" r="1.2" fill="#fff"/></svg>Shopping Cart</div>
<div class="abs top-link" style="left:480px">
  <svg width="11" height="11" viewBox="0 0 12 12"><path d="M1 6l3.5 3.5L11 2" fill="none" stroke="#fff" stroke-width="2"/></svg>Checkout</div>
<div class="abs top-select" style="left:816px;width:109px">
  <span style="width:14px;height:9px;background:#c8d6e8;display:inline-block"></span>English
  <svg width="8" height="6" viewBox="0 0 8 6" style="margin-left:auto"><path d="M0 0h8L4 6z" fill="#fff"/></svg></div>
<div class="abs top-select" style="left:933px;width:101px">
  <span style="width:12px;height:12px;background:#fff;color:var(--green);font-size:9px;line-height:12px;text-align:center">$</span>Dollar
  <svg width="8" height="6" viewBox="0 0 8 6" style="margin-left:auto"><path d="M0 0h8L4 6z" fill="#fff"/></svg></div>

<!-- header -->
<header class="abs header"></header>
<div class="abs logo">LO<span>GO</span></div>
<div class="abs account">LOG IN <em>or</em> CREAT ACCOUNT</div>
<div class="abs head-icon" style="left:942px"><span class="abs badge">0</span>
  <svg width="24" height="24" viewBox="0 0 24 24"><path d="M6 17l2-5 8-8 3 3-8 8z" fill="none" stroke="#6b9a1e" stroke-width="2"/></svg></div>
<div class="abs head-icon" style="left:977px"><span class="abs badge">0</span>
  <svg width="24" height="24" viewBox="0 0 24 24"><path d="M3 5h3l2 9h10l2-7H7" fill="none" stroke="#6b9a1e" stroke-width="2"/><circle cx="10" cy="18" r="1.6" fill="#6b9a1e"/><circle cx="16" cy="18" r="1.6" fill="#6b9a1e"/></svg></div>

<!-- nav -->
<nav class="abs nav"></nav>
<div class="abs nav-item" style="left:170px">SMART PHONE</div>
<div class="abs nav-item active" style="left:289px">DASKTOP</div>
<div class="abs nav-item" style="left:390px">LAPTOP</div>
<div class="abs nav-item" style="left:474px">ACCESSORIES</div>
<div class="abs nav-item" style="left:595px">NETWORKING</div>
<div class="abs nav-item" style="left:720px">SOFTWARE</div>
<div class="abs search">Search Your Item.........</div>
<div class="abs search-btn"><svg width="27" height="24" viewBox="0 0 27 24"><circle cx="12" cy="10.5" r="5" fill="none" stroke="#fff" stroke-width="2"/><path d="M15.5 14l4.5 4.5" stroke="#fff" stroke-width="2.5"/></svg></div>

<div class="abs crumb">Home / Desktop</div>

<!-- promo banner -->
<div class="abs promo">
  <div class="abs promo-title">BEST CONFIGURE AND<br>SUPER BRAND</div>
  <div class="abs promo-offer">UP TO<br>50% OFF</div>
</div>

<!-- product grid -->
<div class="abs grid">
  <div class="card"><div class="card-media" role="img" aria-label="Smartphone lying on its side showing a game scene"><i style="left:30px;top:70px;width:140px;height:80px;background:linear-gradient(135deg,#eee,#556 50%,#ddd)"></i></div><div class="card-name">Smart phone primo</div><div class="card-price">&amp;10299</div><div class="stars"><b></b><b></b><b></b><b></b><b></b></div></div>
  <div class="card"><div class="card-media" role="img" aria-label="Upright smartphone with a fiery artwork bursting from the screen"><i style="left:55px;top:20px;width:95px;height:160px;background:linear-gradient(160deg,#ddd,#e35a1a 45%,#8a1c08)"></i></div><div class="card-name">Smart phone primo</div><div class="card-price">&amp;10299</div><div class="stars"><b></b><b></b><b></b><b></b><b></b></div></div>
  <div class="card"><div class="card-media" role="img" aria-label="Smartphone flanked by speakers"><i style="left:30px;top:40px;width:140px;height:130px;background:linear-gradient(180deg,#555,#222 60%,#111)"></i></div><div class="card-name">Smart phone primo</div><div class="card-price">&amp;10299</div><div class="stars"><b></b><b></b><b></b><b></b><b></b></div></div>

  <div class="card"><div class="card-media" role="img" aria-label="White smartphone tilted with colourful screen"><i style="left:15px;top:55px;width:165px;height:95px;background:linear-gradient(135deg,#e8e8e8,#e8c020 35%,#5aa33c 65%,#eee)"></i></div><div class="card-name">Smart phone primo</div><div class="card-price">&amp;10299</div><div class="stars"><b></b><b></b><b></b><b></b><b></b></div></div>
  <div class="card"><div class="card-media" role="img" aria-label="Smartphone lying on its side showing a game scene"><i style="left:30px;top:70px;width:140px;height:80px;background:linear-gradient(135deg,#eee,#556 50%,#ddd)"></i></div><div class="card-name">Smart phone primo</div><div class="card-price">&amp;10299</div><div class="stars"><b></b><b></b><b></b><b></b><b></b></div></div>
  <div class="card"><div class="card-media" role="img" aria-label="Smartphone flanked by speakers"><i style="left:30px;top:40px;width:140px;height:130px;background:linear-gradient(180deg,#555,#222 60%,#111)"></i></div><div class="card-name">Smart phone primo</div><div class="card-price">&amp;10299</div><div class="stars"><b></b><b></b><b></b><b></b><b></b></div></div>

  <div class="card"><div class="card-media" role="img" aria-label="Black smartphone with a sunset home screen"><i style="left:60px;top:20px;width:80px;height:165px;background:linear-gradient(180deg,#333,#c77a2a 35%,#5a3a20 70%,#222)"></i></div><div class="card-name">Smart phone primo</div><div class="card-price">&amp;10299</div><div class="stars"><b></b><b></b><b></b><b></b><b></b></div></div>
  <div class="card"><div class="card-media" role="img" aria-label="Black smartphone at an angle with night sky screen"><i style="left:25px;top:50px;width:150px;height:100px;background:linear-gradient(135deg,#111,#2b3f7a 50%,#111)"></i></div><div class="card-name">Smart phone primo</div><div class="card-price">&amp;10299</div><div class="stars"><b></b><b></b><b></b><b></b><b></b></div></div>
  <div class="card"><div class="card-media" role="img" aria-label="Smartphone lying on its side showing a game scene"><i style="left:30px;top:70px;width:140px;height:80px;background:linear-gradient(135deg,#eee,#556 50%,#ddd)"></i></div><div class="card-name">Smart phone primo</div><div class="card-price">&amp;10299</div><div class="stars"><b></b><b></b><b></b><b></b><b></b></div></div>

  <div class="card"><div class="card-media" role="img" aria-label="White smartphone showing a shopping app"><i style="left:62px;top:20px;width:78px;height:165px;background:linear-gradient(180deg,#eee,#fff 20%,#3a8fa8 55%,#e8e8e8)"></i></div><div class="card-name">Smart phone primo</div><div class="card-price">&amp;10299</div><div class="stars"><b></b><b></b><b></b><b></b><b></b></div></div>
  <div class="card"><div class="card-media" role="img" aria-label="Smartphone lying on its side showing a game scene"><i style="left:30px;top:70px;width:140px;height:80px;background:linear-gradient(135deg,#eee,#556 50%,#ddd)"></i></div><div class="card-name">Smart phone primo</div><div class="card-price">&amp;10299</div><div class="stars"><b></b><b></b><b></b><b></b><b></b></div></div>
  <div class="card"><div class="card-media" role="img" aria-label="Dark smartphone with a football scene on screen"><i style="left:60px;top:15px;width:85px;height:170px;background:linear-gradient(180deg,#333,#8a3a1a 45%,#222)"></i></div><div class="card-name">Smart phone primo</div><div class="card-price">&amp;10299</div><div class="stars"><b></b><b></b><b></b><b></b><b></b></div></div>
</div>

<!-- sidebar -->
<div class="abs side-head" style="top:232px">CATEGORY</div>
<ul class="abs side-list" style="top:275px">
  <li>Smart phone</li><li>Dasktop</li><li class="on">Laptop</li><li>Accessories</li><li>Networking</li><li>Software</li>
</ul>
<div class="abs side-head" style="top:447px">BY BRAND</div>
<ul class="abs side-list boxes" style="top:491px">
  <li>Korvex</li><li class="on">Deltron</li><li>Pomaro</li><li class="on">Azuno</li><li>Sumbre</li><li>Tosvane</li>
</ul>
<div class="abs side-head" style="top:662px">BY PRICE</div>
<ul class="abs side-list" style="top:705px">
  <li>Appll</li><li>$1000 - $2000</li><li class="on">$2000 - $3000</li><li>$3000 - $4000</li><li>$4000 - $5000</li><li>$5000 - $6000</li>
</ul>
<div class="abs ad" style="top:884px;height:283px;padding-top:90px">Add<br>Banner</div>
<div class="abs ad" style="top:1190px;height:117px;padding-top:4px">Add<br>Banner</div>
<div class="abs ad" style="top:1327px;height:283px;padding-top:92px">Add<br>Banner</div>

<!-- features -->
<section class="abs features"></section>
<div class="abs feature" style="left:168px">
  <svg width="32" height="30" viewBox="0 0 32 30"><path d="M2 14 30 2 22 28 15 18z M15 18 30 2" fill="none" stroke="#fff" stroke-width="2"/></svg>
  <div><strong>First Shipping</strong><small>Got you every where</small></div></div>
<div class="abs feature" style="left:388px">
  <svg width="28" height="32" viewBox="0 0 28 32"><path d="M7 14V9a7 7 0 0 1 14 0v5" fill="none" stroke="#fff" stroke-width="3"/><rect x="3" y="14" width="22" height="16" rx="2" fill="#fff"/></svg>
  <div><strong>Secure Store</strong><small>100% Secure Store</small></div></div>
<div class="abs feature" style="left:611px">
  <svg width="32" height="32" viewBox="0 0 32 32"><circle cx="16" cy="16" r="13" fill="none" stroke="#fff" stroke-width="2.5"/><path d="M16 8v8l6 4" fill="none" stroke="#fff" stroke-width="2.5"/></svg>
  <div><strong>Save Time</strong><small>Save Your Time</small></div></div>
<div class="abs feature" style="left:833px">
  <svg width="36" height="28" viewBox="0 0 36 28"><path d="M1 3h20v17H1z M21 9h8l6 6v5H21z" fill="#fff"/><circle cx="8" cy="23" r="3.5" fill="#fff" stroke="#7fae2c" stroke-width="2"/><circle cx="28" cy="23" r="3.5" fill="#fff" stroke="#7fae2c" stroke-width="2"/></svg>
  <div><strong>Pay on Delivery</strong><small>Got you every where</small></div></div>

<!-- brands -->
<div class="abs section-title">OUR BRAND</div>
<div class="abs brand" style="left:166px"><i></i>Nordbyte</div>
<div class="abs brand" style="left:314px"><i></i>Voltaro</div>
<div class="abs brand" style="left:462px"><i></i>Circuwave</div>
<div class="abs brand" style="left:610px"><i></i>Nordbyte</div>
<div class="abs brand" style="left:758px"><i></i>Lumetra</div>
<div class="abs brand" style="left:906px"><i></i>Kinetiq</div>

<!-- footer -->
<footer class="abs footer"></footer>
<div class="abs foot-col" style="left:168px"><h4>INFORMATION</h4>
  <ul><li>About Us</li><li>Customer Service</li><li>Privacy Policy</li><li>Site Map</li><li>Contact</li></ul></div>
<div class="abs foot-col" style="left:388px"><h4>WHY BUY FROM US</h4>
  <ul><li>About Us</li><li>Shipping &amp; Returns</li><li>International Shippinh</li><li>Affiliates</li><li>Group Sales</li></ul></div>
<div class="abs foot-col" style="left:609px"><h4>MY ACCOUNT</h4>
  <ul><li>Sign In</li><li>View Cart</li><li>My Wishlist</li><li>Track My Order</li><li>Help</li></ul></div>
<div class="abs foot-col contact" style="left:831px"><h4>CONTACT</h4>
  <ul>
    <li><svg width="10" height="13" viewBox="0 0 10 13"><path d="M5 0a5 5 0 0 1 5 5c0 3-5 8-5 8S0 8 0 5a5 5 0 0 1 5-5z" fill="#444"/><circle cx="5" cy="5" r="1.8" fill="#e8e8e8"/></svg>14 Harbor Lane, Westfield,<br>Dorran 2045</li>
    <li style="margin-top:8px"><svg width="10" height="13" viewBox="0 0 10 13"><rect x="1" y="0" width="8" height="13" rx="1.5" fill="#444"/><rect x="2.5" y="2" width="5" height="7" fill="#e8e8e8"/></svg>+00 1555 010 234<br>+00 1555 010 877</li>
    <li style="margin-top:8px"><svg width="12" height="10" viewBox="0 0 12 10"><rect width="12" height="9" fill="#444"/><path d="M0 0l6 5 6-5" fill="none" stroke="#e8e8e8"/></svg><span style="text-transform:none">hello@shopmail.example</span></li>
  </ul></div>

<div class="abs paybar"></div>
<div class="abs tag" style="left:166px;width:113px">WE ACCEPT</div>
<div class="abs pay" style="left:293px">Paycard</div>
<div class="abs pay" style="left:352px">Duocard</div>
<div class="abs pay" style="left:411px">Trustpay</div>
<div class="abs pay" style="left:470px">Cashline</div>
<div class="abs tag" style="left:611px;width:109px">FLLOW US</div>
<div class="abs social" style="left:737px;background:#3b5a98">Vibe</div>
<div class="abs social" style="left:779px;background:#2aa3df">Chirp</div>
<div class="abs social" style="left:821px;background:#d3443a">Plusly</div>
<div class="abs social" style="left:863px;background:#1f6fd6">Show</div>
<div class="abs social" style="left:905px;background:#e06a9b">Dotty</div>

<div class="abs copy">Copyright by : company name</div>

</body>
</html>
```